Get me out of Jail business cards!!!!

I need business cards done for my business. I own a BailBonds and I get people out of jail!

Colors are red white and black

I need it to say on the card these details:

Freedom Hop Bailbonds

427 S Calloway St
Arcadia, FL 34266

863-555-0187

Open 24/7

On the back of the card:

Must check in every Tuesday.

______/______/______ court date
____________________ time
You must know your court date at all times!

Marla Whitcombe - owner
Jolene Whitcombe - agent
Rosalind Pickett - agent

Industry/Entity Type

Bail bonds

Contact Information for Business Card

Colors are red white and black I need it to say on the card these details: Freedom Hop Bailbonds 427 S Calloway St Arcadia, FL 34266 863-555-0187 Open 24/7 On the back of the card: Must check in every Tuesday. ______/______/______ court date ____________________ time You must know your court date at all times! Marla Whitcombe - owner Jolene Whitcombe - agent Rosalind Pickett - agent

Font styles to use
Serif
Sans Serif

Colors
EB3D1F
EC4F4E
F09395
F8D3D4
FCEDEE

Requirements
Must have
• I listed the must haves in the business card details
Nice to have
• Handcuffs or jail bars or a man in a black and white suit

```html
<!DOCTYPE html>
<html lang="en">
<head>
<meta charset="utf-8">
<title>Freedom Hop Bailbonds – Business Cards</title>
<link rel="stylesheet" href="https://fonts.googleapis.com/css2?family=Montserrat:wght@300;400;600;700;800&display=swap">
<style>
  :root {
    --ink: #0b0b0b;
    --card-dark: #161616;
    --card-mid: #2a2a2a;
    --red: #e0302f;
    --white: #ffffff;
    --soft-white: #e8e8e8;
    --muted: #bdbdbd;
    --page: #e7e4e1;
  }
  * { box-sizing: border-box; margin: 0; padding: 0; }
  html, body { width: 1200px; height: 900px; overflow: hidden; }
  body {
    background: var(--page);
    font-family: "Montserrat", Arial, sans-serif;
    position: relative;
  }
  .card {
    position: absolute;
    left: 285px;
    width: 630px;
    height: 360px;
    border-radius: 20px;
    overflow: hidden;
    background: var(--card-dark);
    box-shadow: 0 14px 30px rgba(0,0,0,0.25);
    color: var(--white);
  }
  .card--back { top: 50px; }
  .card--front { top: 470px; }

  .brand {
    font-weight: 800;
    letter-spacing: 0.5px;
    text-transform: uppercase;
    white-space: nowrap;
  }
  .brand .accent, .accent { color: var(--red); }

  /* Back side */
  .back-scene {
    position: absolute; inset: 0;
    background:
      linear-gradient(90deg, rgba(255,255,255,0.04) 0 2%, transparent 2% 14%),
      radial-gradient(ellipse at 40% 60%, #4a4a4a 0%, #262626 45%, #121212 100%);
  }
  .card--back .brand {
    position: absolute; left: 60px; top: 72px;
    font-size: 36px;
  }
  .checkin-band {
    position: absolute; left: 0; right: 0; top: 140px; height: 140px;
    background: var(--white);
    color: var(--ink);
    text-align: center;
    padding-top: 20px;
  }
  .checkin-title {
    font-weight: 700; font-size: 19px; text-transform: uppercase; letter-spacing: 0.3px;
  }
  .fill-line {
    margin-top: 14px;
    font-size: 19px;
    font-weight: 400;
    display: flex; justify-content: center; align-items: flex-end; gap: 6px;
  }
  .blank { display: inline-block; border-bottom: 1.5px solid var(--ink); height: 18px; }
  .fill-line + .fill-line { margin-top: 6px; }
  .reminder {
    position: absolute; left: 0; right: 0; top: 300px;
    text-align: center; font-weight: 300; font-size: 17px; color: var(--soft-white);
  }

  /* Front side */
  .front-bg {
    position: absolute; inset: 0;
    background: linear-gradient(160deg, #2c2c2c 0%, #101010 55%, #0a0a0a 100%);
  }
  .suit-photo {
    position: absolute; right: 0; top: 0; width: 270px; height: 100%;
    background: linear-gradient(90deg, rgba(10,10,10,1) 0%, #1d1d1d 35%, #2b2b2b 65%, #141414 100%);
  }
  .rule {
    position: absolute; left: 42px; width: 5px; background: var(--red);
  }
  .rule--a { top: 0; height: 56px; }
  .rule--b { top: 112px; height: 78px; }
  .rule--c { top: 230px; height: 40px; }
  .card--front .brand {
    position: absolute; left: 56px; top: 68px; font-size: 30px;
  }
  .person { position: absolute; left: 90px; top: 150px; }
  .person-name { font-weight: 800; font-size: 24px; text-transform: uppercase; }
  .person-role { font-weight: 400; font-size: 17px; color: var(--soft-white); margin-top: 2px; }
  .contact { position: absolute; left: 110px; top: 242px; font-size: 22px; font-weight: 400; }
  .phone { display: flex; align-items: center; gap: 12px; }
  .address { margin-top: 12px; line-height: 1.25; }
  .open-badge {
    position: absolute; right: 32px; bottom: 40px;
    display: flex; align-items: center; gap: 10px;
  }
  .open-word { font-weight: 800; font-size: 30px; }
  .open-hours { position: relative; width: 78px; height: 62px; }
  .open-hours svg { position: absolute; inset: 0; }
  .open-hours .num {
    position: absolute; left: 2px; top: 6px; font-weight: 800; font-size: 24px;
  }
  .open-hours .label {
    position: absolute; left: 8px; top: 36px; font-weight: 700; font-size: 10px; letter-spacing: 0.5px;
  }
</style>
</head>
<body>

  <section class="card card--back">
    <div class="back-scene" role="img" aria-label="Dark photo of jail cell bars with handcuffs in the foreground"></div>
    <h2 class="brand">Freedom Hop <span class="accent">Bailbonds</span></h2>
    <div class="checkin-band">
      <p class="checkin-title">Must check in every <span class="accent">Tuesday.</span></p>
      <p class="fill-line">
        <span class="blank" style="width:60px"></span>/<span class="blank" style="width:60px"></span>/<span class="blank" style="width:60px"></span>
        <span>Court Date</span>
      </p>
      <p class="fill-line">
        <span class="blank" style="width:200px"></span>
        <span>Time</span>
      </p>
    </div>
    <p class="reminder">You must know your court date at all Times!</p>
  </section>

  <section class="card card--front">
    <div class="front-bg"></div>
    <div class="suit-photo" role="img" aria-label="Black and white photo of a man in a dark suit buttoning his jacket"></div>
    <span class="rule rule--a"></span>
    <span class="rule rule--b"></span>
    <span class="rule rule--c"></span>
    <h2 class="brand">Freedom Hop <span class="accent">Bailbonds</span></h2>
    <div class="person">
      <p class="person-name">Marla <span class="accent">Whitcombe</span></p>
      <p class="person-role">Owner</p>
    </div>
    <div class="contact">
      <p class="phone">
        <svg width="20" height="20" viewBox="0 0 24 24" aria-hidden="true">
          <path fill="#fff" d="M6.6 10.8a15.1 15.1 0 0 0 6.6 6.6l2.2-2.2c.3-.3.7-.4 1-.2 1.1.4 2.3.6 3.6.6.6 0 1 .4 1 1V20c0 .6-.4 1-1 1C10.6 21 3 13.4 3 4c0-.6.4-1 1-1h3.5c.6 0 1 .4 1 1 0 1.3.2 2.5.6 3.6.1.3 0 .7-.2 1z"/>
        </svg>
        863-555-0187
      </p>
      <p class="address">427 S Calloway St Arcadia<br>FL 34266</p>
    </div>
    <div class="open-badge">
      <span class="open-word">OPEN</span>
      <div class="open-hours">
        <svg viewBox="0 0 78 62" aria-hidden="true">
          <path d="M52 8 A26 26 0 1 1 60 52" fill="none" stroke="#fff" stroke-width="2.5"/>
          <path d="M54 46 L61 53 L52 56" fill="none" stroke="#fff" stroke-width="2.5"/>
        </svg>
        <span class="num">24/7</span>
        <span class="label">HOURS</span>
      </div>
    </div>
  </section>

</body>
</html>
```